Flyer design for the Harvest Lantern Summit 2019 (HALSUM)

Design a flyer for our annual conference with basic information about the conference: conference logo and year, Conference name: Harvest Lantern Summit Location: Talbot Community Center (Downtown Portland)482 Wexley Street, Portland, ME 04109, Date: August 8th, 9th, 10th and 11th, 2019Start time 7:00PMI would like the following three words added to the flyer. These words describe the vision of the conference: Prophetic, Fire, Overflow,

Contact info:
Website: www.vostel.org
Phone: 207 555 3184
Email: contact@meadowcrest.org

Target Market(s)

Young adults living in the United States

Industry/Entity Type

Religious

Font styles to use
Sans Serif

Colors

Designer to choose colors to be used in the design.

Requirements
Must have
• HALSUM must logo standout, the reader should be able to take a quick look and find key info,
Should not have
• Cross image, church image

```html
<!DOCTYPE html>
<html lang="en">
<head>
<meta charset="utf-8">
<title>Harvest Lantern Summit 2019 — Flyer</title>
<link rel="stylesheet" href="https://fonts.googleapis.com/css2?family=Montserrat:wght@700;800&family=Lato:wght@400;700&family=Quicksand:wght@700&display=swap">
<style>
  :root {
    --brand-blue: #1670c0;
    --sky-blue: #1a9ad6;
    --deep-blue: #1d55ad;
    --mid-blue: #1a7ccd;
    --label-blue: #92d6ea;
    --orange: #f08a2c;
    --soft-orange: #f5a35a;
    --cream: #fde3c2;
    --highlight: #f6d31c;
    --white: #ffffff;
    --paper-grey: #e4e5e7;
  }
  * { margin: 0; padding: 0; box-sizing: border-box; }
  html, body { width: 1200px; height: 1200px; overflow: hidden; background: var(--white); }
  .flyer {
    position: absolute; left: 178px; top: 54px;
    width: 844px; height: 1092px; overflow: hidden;
    font-family: "Lato", sans-serif;
  }
  .flyer-bg { position: absolute; inset: 0; }
  .logo-name {
    position: absolute; left: 0; width: 844px; top: 88px; text-align: center;
    font-family: "Montserrat", sans-serif; font-weight: 800; font-size: 88px;
    letter-spacing: 1px; color: var(--brand-blue); line-height: 1;
  }
  .logo-year {
    position: absolute; left: 0; width: 844px; top: 168px;
    display: flex; justify-content: center; align-items: center; gap: 18px;
    font-family: "Montserrat", sans-serif; font-weight: 800; font-size: 40px;
    color: var(--orange); letter-spacing: 26px; line-height: 1;
  }
  .logo-year span { margin-right: -26px; }
  .logo-year .rule { width: 96px; height: 4px; background: var(--orange); }
  .event-name {
    position: absolute; left: 0; width: 844px; top: 226px; text-align: center;
    font-family: "Montserrat", sans-serif; font-weight: 800; font-size: 38px;
    color: var(--orange); letter-spacing: 1px; line-height: 1;
  }
  .event-type {
    position: absolute; left: 0; width: 844px; top: 272px; text-align: center;
    font-family: "Montserrat", sans-serif; font-weight: 700; font-size: 23px;
    color: var(--sky-blue); letter-spacing: 1.5px; line-height: 1;
  }
  .pillar { position: absolute; width: 260px; text-align: center; }
  .pillar-badge {
    width: 116px; height: 116px; margin: 0 auto; border-radius: 50%;
    background: var(--white); box-shadow: 0 6px 14px rgba(0,0,0,0.3);
    display: flex; align-items: center; justify-content: center;
  }
  .pillar-label {
    margin-top: 26px; font-family: "Montserrat", sans-serif; font-weight: 700;
    font-size: 32px; color: var(--label-blue); line-height: 1;
  }
  .pillar--prophetic { left: 17px; top: 422px; }
  .pillar--fire { left: 278px; top: 457px; }
  .pillar--fire .pillar-label { margin-top: 18px; }
  .pillar--overflow { left: 542px; top: 424px; }
  .details { position: absolute; left: 162px; top: 682px; width: 640px; }
  .detail { position: relative; padding-left: 53px; font-size: 26px; color: var(--white); line-height: 33px; }
  .detail-icon {
    position: absolute; left: 0; top: 1px; width: 36px; height: 36px; border-radius: 50%;
    background: var(--soft-orange); box-shadow: 0 2px 4px rgba(0,0,0,0.3);
    display: flex; align-items: center; justify-content: center;
  }
  .detail .accent { color: var(--highlight); }
  .detail--date { margin-top: 33px; }
  .detail--time { margin-top: 33px; }
  .contact-bar {
    position: absolute; left: 0; top: 1044px; width: 844px; height: 36px;
    font-family: "Quicksand", sans-serif; font-weight: 700; font-size: 19.5px; color: var(--white);
  }
  .contact-item { position: absolute; top: 0; display: flex; align-items: center; gap: 8px; height: 36px; }
  .contact-item--phone { left: 34px; }
  .contact-item--email { left: 256px; }
  .contact-item--web { left: 594px; }
</style>
</head>
<body>
<main class="flyer">
  <svg class="flyer-bg" width="844" height="1092" viewBox="0 0 844 1092" aria-hidden="true">
    <defs>
      <linearGradient id="paperGrad" x1="0" y1="0" x2="0" y2="1">
        <stop offset="0" stop-color="#fafafa"/>
        <stop offset="1" stop-color="#e2e3e5"/>
      </linearGradient>
      <linearGradient id="bandGrad" x1="0" y1="0" x2="0" y2="1">
        <stop offset="0" stop-color="#f6a24e"/>
        <stop offset="1" stop-color="#fde6c8"/>
      </linearGradient>
      <radialGradient id="blueGrad" cx="0.5" cy="0.5" r="0.7">
        <stop offset="0" stop-color="#1a86d4"/>
        <stop offset="1" stop-color="#1d52aa"/>
      </radialGradient>
      <linearGradient id="footGrad" x1="0" y1="0" x2="0" y2="1">
        <stop offset="0" stop-color="#f39a3e"/>
        <stop offset="1" stop-color="#ef8a2a"/>
      </linearGradient>
    </defs>
    <rect class="paper" width="844" height="420" fill="url(#paperGrad)"/>
    <path class="top-band" d="M0,274 Q422,370 844,274 V420 H0 Z" fill="url(#bandGrad)"/>
    <path class="blue-field" d="M0,330 Q422,402 844,330 V1092 H0 Z" fill="url(#blueGrad)"/>
    <path class="bottom-shade" d="M0,960 Q422,900 844,960 V1092 H0 Z" fill="#163f86" opacity="0.35"/>
    <path class="bottom-band" d="M0,1010 Q422,926 844,1010 V1092 H0 Z" fill="var(--cream)"/>
    <path class="footer-field" d="M0,1024 Q422,952 844,1024 V1092 H0 Z" fill="url(#footGrad)"/>
  </svg>

  <h1 class="logo-name">HALSUM</h1>
  <div class="logo-year"><i class="rule"></i><span>2019</span><i class="rule"></i></div>
  <h2 class="event-name">HARVEST LANTERN</h2>
  <p class="event-type">SUMMIT</p>

  <div class="pillar pillar--prophetic">
    <div class="pillar-badge">
      <svg width="80" height="70" viewBox="0 0 80 70" aria-hidden="true">
        <path d="M40,68 L8,36 C-4,24 4,4 20,4 C30,4 36,10 40,16 C44,10 50,4 60,4 C76,4 84,24 72,36 Z" fill="var(--soft-orange)"/>
        <path d="M40,52 L26,38 C20,32 24,24 31,24 C35,24 38,27 40,30 C42,27 45,24 49,24 C56,24 60,32 54,38 Z" fill="var(--white)"/>
      </svg>
    </div>
    <p class="pillar-label">PROPHETIC</p>
  </div>

  <div class="pillar pillar--fire">
    <div class="pillar-badge">
      <svg width="76" height="76" viewBox="0 0 76 76" aria-hidden="true">
        <circle cx="38" cy="38" r="16" fill="var(--soft-orange)"/>
        <g stroke="var(--soft-orange)" stroke-width="5" stroke-linecap="round">
          <path d="M38,4 V14 M38,62 V72 M4,38 H14 M62,38 H72 M14,14 L21,21 M55,55 L62,62 M62,14 L55,21 M21,55 L14,62"/>
        </g>
      </svg>
    </div>
    <p class="pillar-label">FIRE</p>
  </div>

  <div class="pillar pillar--overflow">
    <div class="pillar-badge">
      <svg width="76" height="76" viewBox="0 0 76 76" aria-hidden="true">
        <path d="M14,28 H62 L56,66 Q55,70 51,70 H25 Q21,70 20,66 Z" fill="var(--soft-orange)"/>
        <path d="M10,24 Q38,14 66,24 L66,30 H10 Z" fill="var(--soft-orange)"/>
        <circle cx="8" cy="40" r="4" fill="var(--soft-orange)"/>
        <circle cx="68" cy="44" r="4" fill="var(--soft-orange)"/>
        <circle cx="38" cy="8" r="4" fill="var(--soft-orange)"/>
      </svg>
    </div>
    <p class="pillar-label">OVERFLOW</p>
  </div>

  <section class="details">
    <div class="detail detail--venue">
      <span class="detail-icon">
        <svg width="20" height="22" viewBox="0 0 20 22" aria-hidden="true">
          <path d="M10,21 C4,14 2,11 2,8 A8,8 0 0 1 18,8 C18,11 16,14 10,21 Z" fill="none" stroke="#fff" stroke-width="1.6"/>
          <circle cx="10" cy="8" r="3" fill="none" stroke="#fff" stroke-width="1.6"/>
        </svg>
      </span>
      <span class="accent">Talbot Community Center</span><br>
      (Downtown Portland)<br>
      482 Wexley Street, Portland, ME 04109
    </div>
    <div class="detail detail--date">
      <span class="detail-icon">
        <svg width="20" height="18" viewBox="0 0 20 18" aria-hidden="true">
          <rect x="1" y="2" width="18" height="15" rx="1.5" fill="none" stroke="#fff" stroke-width="1.6"/>
          <line x1="1" y1="6" x2="19" y2="6" stroke="#fff" stroke-width="1.6"/>
          <path d="M4,9h2M8,9h2M12,9h2M4,12h2M8,12h2M12,12h2" stroke="#fff" stroke-width="1.6"/>
        </svg>
      </span>
      August 8th, 9th, 10th and 11th, 2019
    </div>
    <div class="detail detail--time">
      <span class="detail-icon">
        <svg width="22" height="22" viewBox="0 0 22 22" aria-hidden="true">
          <circle cx="11" cy="11" r="9" fill="none" stroke="#fff" stroke-width="1.6"/>
          <path d="M11,5 V11 L15,14" fill="none" stroke="#fff" stroke-width="1.6"/>
        </svg>
      </span>
      Start Time <span class="accent">7:00 PM</span>
    </div>
  </section>

  <footer class="contact-bar">
    <div class="contact-item contact-item--phone">
      <svg width="22" height="26" viewBox="0 0 22 26" aria-hidden="true">
        <path d="M6,2 L10,8 L7,11 Q9,17 14,20 L17,17 L21,22 L17,25 Q4,22 2,6 Z" fill="#fff"/>
      </svg>
      <span>(207) 555 3184</span>
    </div>
    <div class="contact-item contact-item--email">
      <svg width="30" height="20" viewBox="0 0 30 20" aria-hidden="true">
        <rect x="1" y="1" width="28" height="18" fill="none" stroke="#fff" stroke-width="2"/>
        <path d="M1,1 L15,12 L29,1 M1,19 L11,9 M29,19 L19,9" fill="none" stroke="#fff" stroke-width="2"/>
      </svg>
      <span>contact@meadowcrest.org</span>
    </div>
    <div class="contact-item contact-item--web">
      <svg width="28" height="28" viewBox="0 0 28 28" aria-hidden="true">
        <g fill="none" stroke="#fff" stroke-width="1.6">
          <circle cx="14" cy="14" r="12"/>
          <ellipse cx="14" cy="14" rx="5" ry="12"/>
          <path d="M2,14 H26 M4,8 H24 M4,20 H24 M14,2 V26"/>
        </g>
      </svg>
      <span>www.vostel.org</span>
    </div>
  </footer>
</main>
</body>
</html>
```